Quarvella Brochure Design - IT Services - Modern Design - Services List

Hi,

We are looking for a modern IT Services brochure design of between 4 - 6 pages, it must be based on a blue and white colour theme with some nice technical imagery. It would need a section about why Quarvella and a contact section at the end.

Here is some info that could be included

Target Market(s)

Medium to Large Businesses

Industry/Entity Type

Information Technology

Colors
0054AA
0677BA
7BADD7
CADEEF
E8F1F8

Requirements
Must have
• Striking technical imagery
Nice to have
• Nice Icons to list the different services sections

```html
<!DOCTYPE html>
<html lang="en">
<head>
<meta charset="utf-8">
<title>Quarvella IT Services Brochure</title>
<link rel="stylesheet" href="https://fonts.googleapis.com/css2?family=Poppins:wght@400;500;600;700&display=swap">
<style>
:root{
  --brand:#0054AA;
  --brand-mid:#0677BA;
  --brand-soft:#7BADD7;
  --brand-pale:#CADEEF;
  --brand-mist:#E8F1F8;
  --navy:#0A2E5C;
  --white:#ffffff;
}
*{box-sizing:border-box;margin:0;padding:0}
html,body{width:1200px;height:848px;overflow:hidden;background:var(--white)}
body{font-family:'Poppins',sans-serif;color:var(--brand);position:relative}
.abs{position:absolute}

/* Cover panel */
.cover{left:74px;top:52px;width:264px;height:746px;background:var(--brand)}
.cover-photo{left:0;top:0;width:264px;height:472px;background:linear-gradient(160deg,#f2f5f8 0%,#dfe8f1 35%,#b9d0e6 70%,#8fb6da 100%)}
.cover-photo-edge{left:0;top:470px;width:264px;height:4px;background:var(--brand-mid)}
.brand-name{left:150px;top:22px;font-size:20px;font-weight:600;color:var(--brand);line-height:1}
.cover-title{left:14px;top:498px;font-size:29px;font-weight:600;color:var(--white);line-height:1.0;border-bottom:1px solid var(--white);padding-bottom:2px;width:170px}
.cover-sub{left:15px;top:566px;font-size:15px;font-weight:400;color:var(--white);line-height:1.0}
.about-title{left:15px;top:620px;font-size:26px;font-weight:600;color:var(--white);border-bottom:1px solid var(--white);width:222px;line-height:1.1}
.about-body{left:15px;top:656px;width:236px;font-size:7.6px;color:var(--white);line-height:1.42}
.cover-foot{left:0;top:717px;width:264px;height:29px;background:var(--navy)}

/* Services spread */
.top-bar{left:338px;top:52px;width:791px;height:16px;background:var(--brand)}
.bottom-band{left:338px;top:782px;width:527px;height:16px;background:var(--navy)}
.services-banner{left:357px;top:111px;width:494px;height:62px;background:var(--brand);color:var(--white);font-size:45px;font-weight:600;padding-left:8px;line-height:62px;letter-spacing:.5px}

.group{width:236px;height:249px;border:1px solid var(--brand);border-top:none}
.group-rule{left:0;top:0;width:100%;height:1px;background:var(--brand)}
.group-head{left:6px;top:-18px;background:var(--white);display:flex;align-items:center;gap:6px;padding-right:4px}
.group-icon{width:30px;height:30px;border:1.5px solid var(--brand);border-radius:50%;display:flex;align-items:center;justify-content:center;background:var(--white)}
.group-title{font-size:17px;font-weight:600;color:var(--brand);line-height:1}
.group-intro{left:9px;top:18px;width:220px;font-size:9.4px;font-weight:500;line-height:1.48;color:var(--brand)}
.tile{width:108px;height:72px;background:var(--brand);color:var(--white);padding:7px 6px}
.tile-head{display:flex;align-items:center;gap:5px;height:22px}
.tile-head svg{flex:none}
.tile-name{font-size:9.6px;font-weight:500;line-height:1;width:74px}
.tile-name.small{font-size:7.6px;line-height:.95}
.tile-desc{font-size:7.3px;line-height:1.1;margin-top:5px;color:var(--brand-mist)}

/* Why choose */
.why-title{left:877px;top:94px;width:239px;height:28px;background:var(--brand);color:var(--white);font-size:17.5px;font-weight:600;padding-left:5px;line-height:28px}
.reason{left:883px;width:230px}
.reason-head{font-size:13.4px;font-weight:600;color:var(--brand);display:flex;align-items:center;gap:6px}
.reason-head::before{content:"";width:5px;height:5px;border-radius:50%;background:var(--brand)}
.reason-body{font-size:6.8px;line-height:1.48;color:var(--brand);margin:6px 0 0 15px;width:200px}

/* Contact */
.contact{left:865px;top:464px;width:264px;height:334px;background:var(--navy);color:var(--white)}
.c-h{left:12px;font-size:23px;font-weight:600;line-height:1}
.c-p{left:19px;font-size:7.8px;line-height:1.5}
.c-list{left:19px;font-size:7.8px;list-style:none;line-height:14.7px}
.c-list li::before{content:"• "}
.c-list li.cont{padding-left:6px}
.c-list li.cont::before{content:""}
.c-list.indent{left:27px}
</style>
</head>
<body>

<section class="abs cover">
  <div class="abs cover-photo" role="img" aria-label="Photo of a smiling support agent wearing a headset, with a colleague behind"></div>
  <div class="abs cover-photo-edge"></div>
  <div class="abs brand-name">Quarvella</div>
  <h1 class="abs cover-title">Quarvella IT Services</h1>
  <p class="abs cover-sub">Empowering Your Business<br>with Cutting-Edge IT Solutions</p>
  <h2 class="abs about-title">About Quarvella</h2>
  <p class="abs about-body">At Quarvella, we are dedicated to providing top-tier IT services that drive efficiency, innovation, and growth for your business. With a commitment to excellence and a team of highly skilled professionals, we offer a comprehensive suite of solutions tailored to meet the unique needs of our clients.</p>
  <div class="abs cover-foot"></div>
</section>

<div class="abs top-bar"></div>
<div class="abs bottom-band"></div>
<h2 class="abs services-banner">Our Services</h2>

<!-- Managed IT -->
<section class="abs group" style="left:351px;top:215px">
  <div class="abs group-rule"></div>
  <div class="abs group-head">
    <div class="group-icon"><svg width="16" height="16" viewBox="0 0 16 16" fill="none" stroke="#0054AA" stroke-width="1.6" stroke-linecap="round"><path d="M3 13 L9 7"/><path d="M9 7a3 3 0 1 1 3 -4"/><path d="M13 13 L4 4"/><path d="M2 2l2 2"/></svg></div>
    <h3 class="group-title">Managed IT Services</h3>
  </div>
  <p class="abs group-intro">Our Managed IT Services provide proactive<br>monitoring and management of your IT<br>infrastructure,ensuring maximum uptime<br>and reliability. We offer:</p>
  <div class="abs tile" style="left:6px;top:86px">
    <div class="tile-head"><svg width="20" height="20" viewBox="0 0 20 20" fill="none" stroke="#fff" stroke-width="1.6"><circle cx="10" cy="10" r="8"/><path d="M10 5v5l3 2"/></svg><span class="tile-name">24/7 Network Monitoring</span></div>
    <p class="tile-desc">Continuous monitoring to detect and resolve issues before they impact your business.</p>
  </div>
  <div class="abs tile" style="left:123px;top:86px">
    <div class="tile-head"><svg width="20" height="20" viewBox="0 0 20 20" fill="none" stroke="#fff" stroke-width="1.6" stroke-linejoin="round"><path d="M4 3l3 0 1 4-2 1.5a9 9 0 0 0 5 5L12.5 11l4 1v3c0 1-1 2-2 2A13 13 0 0 1 3 5c0-1 0-2 1-2z"/><path d="M12 3a5 5 0 0 1 5 5M12 6a2 2 0 0 1 2 2"/></svg><span class="tile-name">Helpdesk<br>Support</span></div>
    <p class="tile-desc">Responsive and knowledgeable support team available round the clock.</p>
  </div>
  <div class="abs tile" style="left:6px;top:170px">
    <div class="tile-head"><svg width="22" height="20" viewBox="0 0 22 20" fill="none" stroke="#fff" stroke-width="1.8" stroke-linecap="round"><path d="M2 5h13M2 10h10M2 15h7M12 14l3 3 6-7"/></svg><span class="tile-name">Patch Management</span></div>
    <p class="tile-desc">Regular updates and patches to keep your systems secure and up-to-date.</p>
  </div>
  <div class="abs tile" style="left:123px;top:170px">
    <div class="tile-head"><svg width="20" height="20" viewBox="0 0 20 20" fill="none" stroke="#fff" stroke-width="1.6"><rect x="2" y="3" width="16" height="14"/><path d="M2 7h16M7 11h6"/></svg><span class="tile-name">IT Asset Management</span></div>
    <p class="tile-desc">Comprehensive tracking and management of your IT assets.</p>
  </div>
</section>

<!-- Cybersecurity -->
<section class="abs group" style="left:615px;top:215px">
  <div class="abs group-rule"></div>
  <div class="abs group-head">
    <div class="group-icon"><svg width="16" height="18" viewBox="0 0 16 18" fill="none" stroke="#0054AA" stroke-width="1.6"><path d="M8 1l6 2.5v5c0 4-3 7-6 8.5-3-1.5-6-4.5-6-8.5v-5z"/></svg></div>
    <h3 class="group-title">Cybersecurity</h3>
  </div>
  <p class="abs group-intro">Protect your business from evolving<br>threats with our comprehensive<br>cybersecurity services.<br>We offer:</p>
  <div class="abs tile" style="left:5px;top:86px">
    <div class="tile-head"><svg width="20" height="22" viewBox="0 0 20 22" fill="none" stroke="#fff" stroke-width="1.7"><path d="M10 1l8 3v6c0 5-4 9-8 11-4-2-8-6-8-11V4z"/><path d="M6 11l3 3 5-6"/></svg><span class="tile-name" style="font-size:8px">Threat Detection and Response</span></div>
    <p class="tile-desc">Advanced threat monitoring and response to safeguard your data.</p>
  </div>
  <div class="abs tile" style="left:122px;top:86px">
    <div class="tile-head"><svg width="20" height="20" viewBox="0 0 20 20" fill="none" stroke="#fff" stroke-width="1.7"><circle cx="6" cy="14" r="4"/><path d="M9 11l8-8M14 6l2 2M16 4l2 2"/></svg><span class="tile-name" style="font-size:7.8px">Security Audits and Assessments</span></div>
    <p class="tile-desc">Thorough evaluations to identify and mitigate vulnerabilities.</p>
  </div>
  <div class="abs tile" style="left:5px;top:170px">
    <div class="tile-head"><svg width="20" height="20" viewBox="0 0 20 20" fill="none" stroke="#fff" stroke-width="1.7"><circle cx="10" cy="10" r="6"/><circle cx="10" cy="10" r="2.5" fill="#fff"/><path d="M10 1v3M10 16v3M1 10h3M16 10h3"/></svg><span class="tile-name">Endpoint Protection</span></div>
    <p class="tile-desc">Robust security solutions for all your devices.</p>
  </div>
  <div class="abs tile" style="left:122px;top:170px">
    <div class="tile-head"><svg width="20" height="22" viewBox="0 0 20 22" fill="none" stroke="#fff" stroke-width="1.7"><path d="M10 1l8 3v6c0 5-4 9-8 11-4-2-8-6-8-11V4z"/><path d="M10 7v7M6.5 10.5h7"/></svg><span class="tile-name small">Compliance<br>and Regulatory<br>Services</span></div>
    <p class="tile-desc">Ensure adherence to industry standards and regulations.</p>
  </div>
</section>

<!-- Cloud -->
<section class="abs group" style="left:351px;top:508px;height:252px">
  <div class="abs group-rule"></div>
  <div class="abs group-head">
    <div class="group-icon"><svg width="18" height="14" viewBox="0 0 18 14" fill="none" stroke="#0054AA" stroke-width="1.6"><path d="M4.5 12.5a3.5 3.5 0 0 1 0-7 5 5 0 0 1 9.5 1.5 2.8 2.8 0 0 1 0 5.5z"/></svg></div>
    <h3 class="group-title">Cloud Solutions</h3>
  </div>
  <p class="abs group-intro">Embrace the power of the<br>cloud with our scalable and<br>secure cloud solutions.<br>Our offerings include:</p>
  <div class="abs tile" style="left:6px;top:86px">
    <div class="tile-head"><svg width="22" height="18" viewBox="0 0 22 18" fill="none" stroke="#fff" stroke-width="1.7"><path d="M6 15a4 4 0 0 1 0-8 6 6 0 0 1 11 2 3 3 0 0 1 0 6"/><path d="M11 17V9M8 12l3-3 3 3"/></svg><span class="tile-name">Cloud<br>Migration</span></div>
    <p class="tile-desc">Seamless transition of your applications and data to the cloud.</p>
  </div>
  <div class="abs tile" style="left:123px;top:86px">
    <div class="tile-head"><svg width="22" height="18" viewBox="0 0 22 18" fill="none" stroke="#fff" stroke-width="1.7"><path d="M6 15a4 4 0 0 1 0-8 6 6 0 0 1 11 2 3 3 0 0 1 0 6"/><path d="M11 8v8M8 13l3 3 3-3"/></svg><span class="tile-name">Cloud<br>Hosting</span></div>
    <p class="tile-desc">Reliable and scalable hosting solutions to meet your growing needs.</p>
  </div>
  <div class="abs tile" style="left:6px;top:170px">
    <div class="tile-head"><svg width="22" height="18" viewBox="0 0 22 18" fill="none" stroke="#fff" stroke-width="1.7"><path d="M2 9l3-7h12l3 7v7H2z"/><path d="M2 9h18"/><circle cx="6" cy="13" r=".8" fill="#fff"/></svg><span class="tile-name small">Backup<br>and Disaster<br>Recovery</span></div>
    <p class="tile-desc">Robust backup and recovery solutions to ensure business continuity.</p>
  </div>
  <div class="abs tile" style="left:123px;top:170px">
    <div class="tile-head"><svg width="20" height="20" viewBox="0 0 20 20" fill="none" stroke="#fff" stroke-width="1.7"><rect x="2" y="3" width="16" height="14" rx="1"/><path d="M8 8l-2 2 2 2M12 8l2 2-2 2"/></svg><span class="tile-name">Software as a Service</span></div>
    <p class="tile-desc">Access to the latest software applications without the hassle of maintenance.</p>
  </div>
</section>

<!-- IT Consulting -->
<section class="abs group" style="left:615px;top:508px;height:249px">
  <div class="abs group-rule"></div>
  <div class="abs group-head">
    <div class="group-icon"><svg width="16" height="16" viewBox="0 0 16 16" fill="none" stroke="#0054AA" stroke-width="1.6"><path d="M2 11V8a6 6 0 0 1 12 0v3"/><rect x="2" y="9" width="3" height="5" fill="#0054AA"/><rect x="11" y="9" width="3" height="5" fill="#0054AA"/></svg></div>
    <h3 class="group-title">IT Consulting</h3>
  </div>
  <p class="abs group-intro">Leverage our expertise to drive<br>your IT strategy and achieve your<br>business goals. Our consulting<br>services include:</p>
  <div class="abs tile" style="left:5px;top:86px">
    <div class="tile-head"><svg width="20" height="20" viewBox="0 0 20 20"><rect x="1" y="1" width="18" height="18" fill="none" stroke="#fff" stroke-width="1.5"/><g fill="#fff"><rect x="3" y="3" width="4" height="4"/><rect x="11" y="3" width="4" height="4"/><rect x="7" y="7" width="4" height="4"/><rect x="3" y="11" width="4" height="4"/><rect x="11" y="11" width="4" height="4"/><rect x="15" y="7" width="2" height="4"/><rect x="7" y="15" width="4" height="2"/></g></svg><span class="tile-name">IT Strategy and Planning</span></div>
    <p class="tile-desc">Strategic guidance to align your IT initiatives with your business objectives.</p>
  </div>
  <div class="abs tile" style="left:122px;top:86px">
    <div class="tile-head"><svg width="20" height="20" viewBox="0 0 20 20" fill="#fff"><text x="0" y="6" font-size="5" font-family="Poppins,sans-serif">1</text><text x="0" y="12" font-size="5" font-family="Poppins,sans-serif">2</text><text x="0" y="18" font-size="5" font-family="Poppins,sans-serif">3</text><rect x="5" y="3" width="14" height="2"/><rect x="5" y="9" width="14" height="2"/><rect x="5" y="15" width="14" height="2"/></svg><span class="tile-name">Technology Assessments</span></div>
    <p class="tile-desc">In-depth evaluations to optimize your IT infrastructure.</p>
  </div>
  <div class="abs tile" style="left:5px;top:170px">
    <div class="tile-head"><svg width="20" height="20" viewBox="0 0 20 20" fill="none" stroke="#fff" stroke-width="1.7" stroke-linejoin="round"><path d="M10 1l8 4v10l-8 4-8-4V5z"/><path d="M2 5l8 4 8-4M10 9v10M6 3l8 4"/></svg><span class="tile-name">Project Management</span></div>
    <p class="tile-desc">Expert management of IT projects from inception to completion.</p>
  </div>
  <div class="abs tile" style="left:122px;top:170px">
    <div class="tile-head"><svg width="20" height="20" viewBox="0 0 20 20" fill="none" stroke="#fff" stroke-width="1.6"><circle cx="10" cy="10" r="8.5"/><circle cx="10" cy="10" r="5"/><circle cx="10" cy="10" r="1.8" fill="#fff"/></svg><span class="tile-name small">Business<br>Continuity<br>Planning</span></div>
    <p class="tile-desc">Strategies to ensure your business remains operational during disruptions.</p>
  </div>
</section>

<!-- Why choose -->
<h2 class="abs why-title">Why Choose Quarvella?</h2>
<div class="abs reason" style="top:137px">
  <h3 class="reason-head">Expertise and Experience</h3>
  <p class="reason-body">With years of experience in the IT industry, our team possesses the knowledge and skills to tackle any challenge. We stay abreast of the latest technological advancements to provide you with cutting-edge solutions.</p>
</div>
<div class="abs reason" style="top:211px">
  <h3 class="reason-head">Customer-Centric Approach</h3>
  <p class="reason-body">We prioritize our clients' needs and work closely with them to deliver customized solutions that drive success. Our client-centric approach ensures that we are always aligned with your business goals.</p>
</div>
<div class="abs reason" style="top:284px">
  <h3 class="reason-head">Proactive Support</h3>
  <p class="reason-body">Our proactive support model ensures that potential issues are identified and resolved before they can impact your operations. We are committed to maintaining the highest levels of service availability and performance.</p>
</div>
<div class="abs reason" style="top:358px">
  <h3 class="reason-head">Comprehensive Solutions</h3>
  <p class="reason-body">From managed services to cybersecurity, we offer a comprehensive suite of IT solutions designed to meet the diverse needs of your business. Our holistic approach ensures that all aspects of your IT infrastructure are covered.</p>
</div>

<!-- Contact -->
<section class="abs contact">
  <h2 class="abs c-h" style="top:11px;font-size:27px">Get in Touch</h2>
  <p class="abs c-p" style="top:44px;width:190px">Discover how Quarvella can transform your IT landscape and drive your business forward. Contact us today to learn more about our services and how we can help you achieve your goals.</p>
  <h2 class="abs c-h" style="top:104px">Contact Us</h2>
  <ul class="abs c-list" style="top:132px">
    <li>Website: www.quarvella-it.example</li>
    <li>Email: hello@quarvella-it.example</li>
    <li>Phone: +44 161 555 0192</li>
    <li>Address: 48 Harbour Lane,</li>
    <li class="cont">Meridian Park, Leeds, UK</li>
  </ul>
  <h2 class="abs c-h" style="top:204px">Follow Us</h2>
  <p class="abs c-p" style="top:228px;line-height:14.7px;width:160px">Stay updated with the latest news and updates from Quarvella:</p>
  <ul class="abs c-list indent" style="top:257px">
    <li>Professional Network: [URL]</li>
    <li>Microblog: [URL]</li>
    <li>Community Page: [URL]</li>
  </ul>
</section>

</body>
</html>
```